Business card for event manager / organizer "velmora tandem"

Draft of a new valuable business card for my company.
Events, personnel service providers, festivals

```html
<!DOCTYPE html>
<html lang="de">
<head>
<meta charset="utf-8">
<title>velmora tandem – Visitenkarte</title>
<link rel="stylesheet" href="https://fonts.googleapis.com/css2?family=Open+Sans:wght@400;600;700&display=swap">
<style>
  :root {
    --backdrop: #e7e4df;
    --card-dark: #050607;
    --card-mid: #17191c;
    --gold: #b8925a;
    --gold-light: #d6b47c;
    --white: #ffffff;
    --muted: #9a9a9a;
    --photo-light: #d9dadc;
    --photo-dark: #3a3c40;
  }
  * { margin: 0; padding: 0; box-sizing: border-box; }
  html, body {
    width: 1200px; height: 900px; overflow: hidden;
    background: var(--backdrop);
    font-family: "Open Sans", Arial, sans-serif;
  }
  .sheet {
    width: 1200px; height: 900px;
    display: flex; flex-direction: column; align-items: center; justify-content: center;
    gap: 44px;
  }
  .card {
    width: 660px; height: 377px; display: block;
    filter: drop-shadow(0 10px 18px rgba(0,0,0,.28));
  }
  .brand-name { font-weight: 700; fill: var(--white); letter-spacing: .5px; }
  .brand-mark { fill: var(--gold); }
  .tagline { fill: var(--muted); font-size: 11px; font-weight: 400; }
  .gold-rule { fill: none; stroke: var(--gold); stroke-width: 3; }
  .person-name { fill: var(--gold-light); font-size: 18px; font-weight: 600; letter-spacing: 1.5px; }
  .person-role { fill: var(--white); font-size: 13px; }
  .contact-text { fill: var(--white); font-size: 13px; }
  .icon { fill: var(--gold); }
  .icon-line { fill: none; stroke: var(--gold); stroke-width: 1.4; }
</style>
</head>
<body>
<main class="sheet">

  <!-- Front side -->
  <svg class="card card-front" viewBox="0 0 600 343" xmlns="http://www.w3.org/2000/svg">
    <defs>
      <linearGradient id="cardBg" x1="0" y1="0" x2="1" y2="1">
        <stop offset="0" stop-color="#1b1d20"/>
        <stop offset=".5" stop-color="#050607"/>
        <stop offset="1" stop-color="#0c0d0f"/>
      </linearGradient>
      <radialGradient id="portraitBg" cx=".6" cy=".35" r=".8">
        <stop offset="0" stop-color="#d9dadc"/>
        <stop offset=".55" stop-color="#7d7f83"/>
        <stop offset="1" stop-color="#2e3034"/>
      </radialGradient>
      <clipPath id="frontClip"><rect width="600" height="343" rx="28"/></clipPath>
    </defs>
    <g clip-path="url(#frontClip)">
      <rect class="card-base" width="600" height="343" fill="url(#cardBg)"/>
      <polygon class="portrait" role="img" aria-label="Portrait des Inhabers in Weste und Fliege mit zwei Sektgläsern"
        points="292,0 600,0 600,343 470,343 292,118" fill="url(#portraitBg)"/>
      <polyline class="gold-rule" points="279,0 279,124 454,343"/>
    </g>
    <g class="brand" transform="translate(38,248)">
      <rect class="brand-mark" x="0" y="0" width="46" height="46"/>
      <text class="brand-name" x="58" y="28" font-size="30">velmora tandem</text>
      <text class="tagline" x="60" y="46">…denn die nächste Feier kommt bestimmt!</text>
    </g>
  </svg>

  <!-- Back side -->
  <svg class="card card-back" viewBox="0 0 600 343" xmlns="http://www.w3.org/2000/svg">
    <defs>
      <linearGradient id="cardBg2" x1="0" y1="0" x2="1" y2="1">
        <stop offset="0" stop-color="#121417"/>
        <stop offset="1" stop-color="#040506"/>
      </linearGradient>
      <radialGradient id="portraitBg2" cx=".5" cy=".3" r=".8">
        <stop offset="0" stop-color="#dcdde0"/>
        <stop offset=".55" stop-color="#808286"/>
        <stop offset="1" stop-color="#2e3034"/>
      </radialGradient>
      <clipPath id="backClip"><rect width="600" height="343" rx="28"/></clipPath>
    </defs>
    <g clip-path="url(#backClip)">
      <rect class="card-base" width="600" height="343" fill="url(#cardBg2)"/>
      <polygon class="portrait" role="img" aria-label="Portrait des Inhabers in Weste und Fliege mit zwei Sektgläsern"
        points="0,112 118,46 255,46 292,128 292,343 0,343" fill="url(#portraitBg2)"/>
      <polyline class="gold-rule" points="120,34 264,34 304,122 304,343"/>
    </g>

    <g class="brand" transform="translate(322,38)">
      <rect class="brand-mark" x="0" y="0" width="36" height="36"/>
      <text class="brand-name" x="45" y="22" font-size="21">velmora tandem</text>
      <text class="tagline" x="46" y="35" font-size="9">…denn die nächste Feier kommt bestimmt!</text>
    </g>

    <text class="person-name" x="352" y="130">LENA BRANDT</text>
    <text class="person-role" x="362" y="150">Inhaber</text>

    <line class="gold-rule" x1="342" y1="122" x2="342" y2="318" stroke-width="2"/>

    <g class="contact-list">
      <rect class="icon-line" x="358" y="170" width="8" height="13" rx="1.5"/>
      <text class="contact-text" x="376" y="182">0170 555 01 23</text>
      <path class="icon" d="M357 201 q5-5 12 0 v3 h-3 v-2 h-6 v2 h-3z M359 204 h8 v5 h-8z"/>
      <text class="contact-text" x="376" y="208">02361 555 04 87</text>
      <rect class="icon-line" x="357" y="224" width="11" height="8"/>
      <polyline class="icon-line" points="357,224 362.5,229 368,224"/>
      <text class="contact-text" x="376" y="233">info@velmora-tandem.de</text>
      <circle class="icon-line" cx="362.5" cy="254" r="5.5"/>
      <line class="icon-line" x1="357" y1="254" x2="368" y2="254"/>
      <text class="contact-text" x="376" y="259">www.velmora-tandem.de</text>
      <path class="icon" d="M362.5 287 q-6-7-6-10.5 a6 6 0 0 1 12 0 q0 3.5-6 10.5z"/>
      <circle cx="362.5" cy="276.5" r="2" fill="#050607"/>
      <text class="contact-text" x="376" y="284">Lindenweg 12, 45657 Musterstadt</text>
      <circle class="icon" cx="362.5" cy="304" r="5.5"/>
      <text class="contact-text" x="376" y="309">/velmoratandem</text>
    </g>
  </svg>

</main>
</body>
</html>
```